Business cards for Remedial Massage Business
Remedial Massage Tolvern
Can high star design please have information of:
Health fund rebates
Designs need to have front and back. Not just front please.
Great work
Thanks :)
check your private massage on top right (1)
thanks
Must have info:
Front white.. black back.. or vice versa..
Great designs all but im going to be picky...
keep up the great work:)
Star rating please.....
Also stationary design would also be great thx
website is not up and running..
this is only for business cards
thx
hey all,
sorry just uploaded winning logo.
Thought it did it for me.
Thanks:)
Hi,
Could you please upload your logo? Or is logo part of the design?
When I go to the web address listed in the brief it just shows as a parked, unused site.

```html
<!DOCTYPE html>
<html lang="en">
<head>
<meta charset="utf-8">
<title>Remedial Massage Tolvern – Business Cards</title>
<link rel="stylesheet" href="https://fonts.googleapis.com/css2?family=Arimo:wght@400;700&display=swap">
<style>
  :root {
    --backdrop: #d9d9db;
    --black: #161616;
    --black-soft: #2a2a2a;
    --orange: #f08a1c;
    --paper: #ffffff;
    --ink: #2b2b2b;
    --ink-soft: #6a6a6a;
    --grey-on-black: #b5b5b5;
  }
  html, body {
    margin: 0;
    padding: 0;
    width: 1200px;
    height: 901px;
    overflow: hidden;
    background: var(--backdrop);
    font-family: "Arimo", Arial, sans-serif;
  }
  .sheet {
    position: relative;
    width: 1200px;
    height: 901px;
  }
  .card {
    position: absolute;
    top: 296px;
    width: 540px;
    height: 309px;
    box-shadow: 0 10px 28px rgba(0,0,0,0.18);
    box-sizing: border-box;
  }

  /* Front side – black */
  .card--front {
    left: 40px;
    background: radial-gradient(circle at 50% 40%, var(--black-soft) 0%, var(--black) 75%);
    display: flex;
    flex-direction: column;
    align-items: center;
    justify-content: center;
    color: var(--paper);
  }
  .brand-mark {
    width: 64px;
    height: 64px;
    border-radius: 50%;
    background: var(--orange);
    margin-bottom: 14px;
  }
  .brand-name {
    font-weight: 700;
    font-size: 24px;
    letter-spacing: 2px;
    text-transform: uppercase;
    text-align: center;
    line-height: 1.15;
  }
  .brand-tagline {
    margin-top: 8px;
    font-size: 9px;
    letter-spacing: 1.5px;
    text-transform: uppercase;
    color: var(--grey-on-black);
  }
  .rebate-note {
    margin-top: 22px;
    padding-top: 10px;
    border-top: 1px solid var(--orange);
    font-size: 10px;
    font-weight: 700;
    letter-spacing: 1.5px;
    text-transform: uppercase;
    color: var(--orange);
  }

  /* Back side – white */
  .card--back {
    left: 620px;
    background: var(--paper);
    display: flex;
    align-items: center;
    padding: 0 28px 0 26px;
  }
  .back-brand {
    width: 210px;
    display: flex;
    flex-direction: column;
    align-items: center;
    color: var(--black);
  }
  .back-brand .brand-mark {
    width: 54px;
    height: 54px;
    margin-bottom: 10px;
  }
  .back-brand .brand-name {
    font-size: 19px;
    letter-spacing: 1.5px;
  }
  .back-brand .brand-tagline {
    color: var(--ink-soft);
    font-size: 7.5px;
    letter-spacing: 1px;
  }
  .divider {
    width: 3px;
    height: 150px;
    background: var(--orange);
    margin: 0 20px 0 18px;
    flex: none;
  }
  .contact {
    color: var(--ink);
  }
  .contact-name {
    font-weight: 700;
    font-size: 17px;
    margin: 0;
  }
  .contact-role {
    font-size: 9px;
    color: var(--ink-soft);
    margin: 3px 0 18px;
  }
  .contact-list {
    list-style: none;
    margin: 0;
    padding: 0;
    font-size: 9.5px;
  }
  .contact-list li {
    display: flex;
    align-items: center;
    gap: 7px;
    margin-bottom: 7px;
  }
  .contact-list li.address { margin-bottom: 16px; }
  .icon {
    width: 11px;
    height: 11px;
    flex: none;
  }
</style>
</head>
<body>
<main class="sheet">
  <section class="card card--front" aria-label="Card front">
    <div class="brand-mark"></div>
    <div class="brand-name">Remedial Massage Tolvern</div>
    <div class="brand-tagline">Your path to feeling better</div>
    <div class="rebate-note">Health fund rebates available</div>
  </section>

  <section class="card card--back" aria-label="Card back">
    <div class="back-brand">
      <div class="brand-mark"></div>
      <div class="brand-name">Remedial Massage Tolvern</div>
      <div class="brand-tagline">Your path to feeling better</div>
    </div>
    <div class="divider"></div>
    <div class="contact">
      <p class="contact-name">Dorian Welbeck</p>
      <p class="contact-role">Remedial Massage Therapist</p>
      <ul class="contact-list">
        <li class="address">
          <svg class="icon" viewBox="0 0 12 12"><path d="M6 1a3.5 3.5 0 0 0-3.5 3.5C2.5 7.5 6 11 6 11s3.5-3.5 3.5-6.5A3.5 3.5 0 0 0 6 1z" fill="#f08a1c"/><circle cx="6" cy="4.5" r="1.3" fill="#fff"/></svg>
          118 Halden Street, Tolvern 2187
        </li>
        <li>
          <svg class="icon" viewBox="0 0 12 12"><path d="M3 1.2l1.6 2.2-1 1.2a6.5 6.5 0 0 0 3.8 3.8l1.2-1 2.2 1.6-.8 1.8C5.5 10.8 1.2 6.5 1.2 2z" fill="#f08a1c"/></svg>
          0491305762
        </li>
        <li>
          <svg class="icon" viewBox="0 0 12 12"><rect x="1" y="2.5" width="10" height="7" rx="1" fill="#f08a1c"/><path d="M1.5 3l4.5 3.5L10.5 3" stroke="#fff" stroke-width="1" fill="none"/></svg>
          hello@tolvernmassage.com
        </li>
        <li>
          <svg class="icon" viewBox="0 0 12 12"><circle cx="6" cy="6" r="5" fill="#f08a1c"/><path d="M1 6h10M6 1c-2 2.5-2 7.5 0 10M6 1c2 2.5 2 7.5 0 10" stroke="#fff" stroke-width=".8" fill="none"/></svg>
          www.tolvernmassage.com.au
        </li>
      </ul>
    </div>
  </section>
</main>
</body>
</html>
```